Bramblewood Coatings of Central Florida, LLC. Start-up painting business needs a professional web desig

We have a start up painting business that would like to reach/focus on commercial clients like building contractors, HOA's, apartment complexes, etc.. We would like a residential aspect to the web design as well. We have an existing website at "trybramblewoodcoats.com" with usable content. Have logo and color scheme attached. Use provided website ONLY as template. Add commercial services page. Can type own content when needed.

Industry/Entity Type

Apartment

Number of Pages Required

5+ page

Font styles to use
Serif
Sans Serif
Decorative
Script

Requirements
Must have
• Commercial services

```html
<!DOCTYPE html>
<html lang="en">
<head>
<meta charset="utf-8">
<title>Bramblewood Coatings of Central Florida, LLC</title>
<link href="https://fonts.googleapis.com/css2?family=Lato:wght@400;700&family=Oswald:wght@500;700&display=swap" rel="stylesheet">
<style>
:root{
  --red:#d83a35;
  --beige:#e9e2da;
  --beige-strip:#e7e0d8;
  --ink:#222;
  --muted:#666;
  --white:#fff;
  --footer:#000;
  --footer-text:#ddd;
  --phone:#444;
  --pattern:#ececec;
}
*{margin:0;padding:0;box-sizing:border-box}
html,body{width:804px;height:1200px;overflow:hidden;background:var(--white)}
body{font-family:'Lato',sans-serif;color:var(--ink);position:relative}
.top-strip{position:absolute;left:0;top:0;width:804px;height:9px;background:var(--beige-strip)}
.site-header{position:absolute;left:0;top:9px;width:804px;height:84px;background:var(--white)}
.brand{position:absolute;left:68px;top:18px;display:flex;align-items:center;gap:14px}
.brand-mark{width:70px;height:52px;background:var(--beige)}
.brand-name{font-size:12px;line-height:15px;color:#333;width:220px;white-space:nowrap}
.main-nav{position:absolute;right:58px;top:58px;display:flex;gap:30px;font-size:10px;text-transform:uppercase;color:#333}
.main-nav .active{color:var(--red)}
.hero{position:absolute;left:0;top:93px;width:804px;height:462px}
.hero-photo{position:absolute;inset:0;background:linear-gradient(180deg,#c8262a 0%,#d22e30 70%,#b8282a 76%,#4f8a2c 80%,#3f7a22 100%)}
.hero-copy{position:absolute;left:393px;top:132px;color:var(--white)}
.hero-flag{position:absolute;left:0;top:-10px;width:29px;height:24px}
.hero-kicker{font-family:'Oswald',sans-serif;font-weight:500;font-size:30px;line-height:34px;margin-top:24px}
.hero-title{font-family:'Oswald',sans-serif;font-weight:700;font-size:54px;line-height:54px;letter-spacing:.5px}
.hero-ribbon{display:flex;align-items:flex-start;margin-top:6px}
.hero-ribbon span{background:var(--red);border:1px solid var(--white);font-family:'Oswald',sans-serif;font-size:14px;letter-spacing:2px;padding:2px 18px;height:22px}
.hero-ribbon svg{margin-left:4px}
.hero-text{font-size:9px;line-height:12px;width:265px;margin-top:-12px}
.hero-dots{display:flex;gap:4px;margin-top:10px}
.hero-dots i{width:11px;height:11px;border-radius:50%;background:var(--white)}
.hero-dots i.off{background:#e9a5a3}
.services{position:absolute;top:592px;left:58px;display:flex;gap:29px}
.service-card{width:210px;height:206px;background:var(--beige);padding:10px 9px}
.service-photo{width:192px;height:114px}
.service-card h3{font-weight:400;font-size:15px;margin:10px 0 2px 0}
.service-card p{font-size:9.5px;line-height:13px;color:var(--muted);height:39px;overflow:hidden}
.feature-band{position:absolute;left:0;top:836px;width:804px;height:249px;background:var(--pattern)}
.feature{position:absolute;top:22px}
.feature h2{font-weight:400;font-size:16px;line-height:20px;white-space:nowrap}
.feature h2 em{font-style:normal;color:var(--red)}
.feature h4{font-weight:400;font-size:12px;margin-top:5px;padding-bottom:6px;border-bottom:1px solid #999}
.feature p{font-size:9.5px;line-height:16px;margin-top:10px;height:128px;overflow:hidden}
.feature-photo{float:left;width:144px;height:88px;margin:0 6px 4px 0;border:2px solid var(--white)}
.read-more{position:absolute;display:flex;align-items:center}
.read-more span{background:var(--red);color:var(--white);font-size:10.5px;padding:4px 10px;height:21px}
.footer-rule{position:absolute;left:0;top:1085px;width:804px;height:5px;background:var(--red)}
.site-footer{position:absolute;left:0;top:1090px;width:804px;height:110px;background:var(--footer);color:var(--footer-text)}
.footer-nav{position:absolute;left:58px;top:21px;display:flex;gap:20px;font-size:9px;color:var(--white)}
.social{position:absolute;left:58px;top:59px;display:flex;gap:9px}
.social i{width:17px;height:17px;border-radius:50%;background:#1c1c1c;border:1px solid #555}
.copyright{position:absolute;left:58px;top:82px;font-size:7.5px;color:#888}
.call{position:absolute;left:606px;top:20px;text-align:center;width:140px}
.call h5{font-weight:400;font-size:18px;color:var(--white)}
.call p{font-weight:700;font-size:17px;color:var(--phone);line-height:22px;margin-top:4px}
</style>
</head>
<body>
<div class="top-strip"></div>
<header class="site-header">
  <div class="brand">
    <div class="brand-mark"></div>
    <div class="brand-name">Bramblewood Coatings of Central<br>FLORIDA, LLC.</div>
  </div>
  <nav class="main-nav"><span class="active">Home</span><span>About Us</span><span>Services</span><span>Contact Us</span></nav>
</header>

<section class="hero">
  <div class="hero-photo" role="img" aria-label="Painter rolling paint onto a red clapboard wall beside an orange ladder, green lawn below"></div>
  <div class="hero-copy">
    <svg class="hero-flag" viewBox="0 0 29 24"><path d="M0 0H29V24L14.5 14L0 24Z" fill="#fff"/></svg>
    <div class="hero-kicker">Where Dreams</div>
    <div class="hero-title">MEET REALITY</div>
    <div class="hero-ribbon"><span>IT IS A LONG ESTABLISHED FACT</span>
      <svg width="30" height="40" viewBox="0 0 30 40"><path d="M0 0H30V40L15 28L0 40Z" fill="#fff"/></svg></div>
    <p class="hero-text">It is a long established fact that a reader will be distracted by the readable content of a page when looking at its layout. The point of</p>
    <div class="hero-dots"><i></i><i></i><i></i><i class="off"></i></div>
  </div>
</section>

<section class="services">
  <article class="service-card">
    <div class="service-photo" role="img" aria-label="Hand scraping peeling white paint from siding" style="background:linear-gradient(135deg,#c9c3b8,#8f8a80)"></div>
    <h3>Repair Services</h3>
    <p>No matter what the project you can always bet there will be repairs needed to provide the best job. We provide all minor repairs unlike</p>
  </article>
  <article class="service-card">
    <div class="service-photo" role="img" aria-label="Painter on a ladder rolling aqua paint onto an interior wall" style="background:linear-gradient(135deg,#bfe6e6,#6fc2c4)"></div>
    <h3>Interior Painting Services</h3>
    <p>Sometimes just a coat of paint is all you may need for a fresh look. Other times you need a little more. With our huge line of interior</p>
  </article>
  <article class="service-card">
    <div class="service-photo" role="img" aria-label="Empty room with warm tan walls and hardwood floor" style="background:linear-gradient(135deg,#c9a26c,#8a6a3e)"></div>
    <h3>Interior Design Services</h3>
    <p>People think painting is the hard part of the job. Try choosing colors with over a millions variations from over 100 manufacturers. The</p>
  </article>
</section>

<section class="feature-band">
  <div class="feature" style="left:58px;width:332px">
    <h2><em>Commercial</em> Services</h2>
    <h4>Bramblewood Coatings of Central Florida, LLC.</h4>
    <p><span class="feature-photo" role="img" aria-label="Couple painting a wall together" style="background:linear-gradient(135deg,#d9dde2,#9fb0c2)"></span>Bramblewood Coatings of Central Florida, LLC. has painted thousands of homes in its day, but the one we're most excited about painting is the one we're painting today. Your home could be that home.Know what you want? Great.<br>We love to execute on a homeowner's vision. Not sure whether to go mild or wild? That's where our consultative approach and vast experience shines. We'll come up</p>
  </div>
  <div class="feature" style="left:411px;width:335px">
    <h2><em>The best home</em> painters are yours for the taking.</h2>
    <h4>Bramblewood Coatings of Central Florida, LLC.</h4>
    <p style="width:290px">Bramblewood Coatings of Central Florida, LLC. has painted thousands of homes in its day, but the one we're most excited about painting is the one we're painting today. Your home could be that home.Know what you want? Great.<br><br>We love to execute on a homeowner's vision. Not sure whether to go mild or wild? That's where our consultative approach and vast experience shines.</p>
  </div>
  <a class="read-more" style="left:58px;top:212px"><span>Read More</span><svg width="10" height="21" viewBox="0 0 10 21"><path d="M0 0H10L4 10.5L10 21H0Z" fill="#d83a35"/></svg></a>
  <a class="read-more" style="left:411px;top:212px"><span>Read More</span><svg width="10" height="21" viewBox="0 0 10 21"><path d="M0 0H10L4 10.5L10 21H0Z" fill="#d83a35"/></svg></a>
</section>

<div class="footer-rule"></div>
<footer class="site-footer">
  <nav class="footer-nav"><span>Home</span><span>About Us</span><span>Services</span><span>Contact us</span></nav>
  <div class="social"><i></i><i></i><i></i><i></i></div>
  <p class="copyright">Copyright © Marlow Finch, All rights reserved</p>
  <div class="call"><h5>Call Us</h5><p>+1.555-210-4478<br>+1.555-387-1265</p></div>
</footer>
</body>
</html>
```